Product label for premium fruit wooden crates

Background: KelVaro offers premium quality fruits airflown (i.e. Japan, USA, Australia, etc) to Singapore at an affordable price. This includes exquisite and limited fruits like Shine Muscat grape, Shizuoka Crown Melon, Yellow Dragon Fruit, Fei zi xiao seedless lychee, Yellow Peaches, etc.

Requirements:

- Design a premium fruit’s label strap for identification and brand marketing.

- This strap will be used to tie around our fruit gift crate and fruit boxes (see attached).

- the logo use in this strap may use different color that must fit the 2 ribbons that will be used together with the crate box (see attached), red and gold ribbons(purl satin)

- the fruit crates and boxes will be presented as gift for vip, families, and working partners (important people)

This label will be printed in paper and tie around the fruit crate or paper box.

Web: www.kelvaro.sg
FB: https://www.facebook.com/kvrorch/
IG: https://www.instagram.com/kvrorch

Target Market(s)

Working class, families, expat, business clients (late 20 – 40s)

Industry/Entity Type

Gift Shop

Font styles to use
Other font styles liked:
• Sakkal Majalla

Requirements
Must have
• - color that fit the 2 ribbons color (red and gold)
• - premium, luxury and exquisite feel
• - presentable as a gift to someone important
• - Kelvaro's logo
• - The word 'KELVARO',
Nice to have
• the following words:
• - www.kelvaro.sg; or/and
• - online premium fruits or/and
• - premium quality (No preference. let the designer choose)
• must be able to give customer a feel that Kelvaro sells premium fruits
Should not have
• cant think of it now

```html
<!DOCTYPE html>
<html lang="en">
<head>
<meta charset="utf-8">
<title>KelVaro Crate Label Strap</title>
<link rel="stylesheet" href="https://fonts.googleapis.com/css2?family=Montserrat:wght@400;500&display=swap">
<style>
  :root {
    --paper: #ffffff;
    --strap-red: #e31b23;
    --strap-red-deep: #c9202a;
    --strap-red-soft: #d81f28;
    --gold: #e6b84c;
    --gold-light: #f6e2a6;
    --ink: #1a1a1a;
  }
  * { margin: 0; padding: 0; box-sizing: border-box; }
  html, body {
    width: 1200px;
    height: 459px;
    overflow: hidden;
    background: var(--paper);
  }
  .canvas {
    position: relative;
    width: 1200px;
    height: 459px;
    background: var(--paper);
    font-family: "Montserrat", Arial, sans-serif;
  }

  /* Dimension annotations */
  .dimension {
    position: absolute;
    font-size: 14px;
    color: var(--ink);
    line-height: 1;
  }
  .dimension--left  { left: 205px; top: 11px; }
  .dimension--mid   { left: 562px; top: 11px; }
  .dimension--right { left: 937px; top: 11px; }
  .dimension--height {
    left: 52px; top: 60px;
    transform: rotate(-90deg);
    transform-origin: center;
  }

  /* Label strap */
  .strap {
    position: absolute;
    background: var(--strap-red);
    overflow: hidden;
  }
  .strap--spec   { left: 88px; top: 28px; width: 1026px; height: 76px; }
  .strap--large  { left: 0; top: 348px; width: 1200px; height: 86px; }

  .strap__rule {
    position: absolute;
    left: 0; right: 0;
    height: 3px;
    background: linear-gradient(90deg, var(--gold-light), var(--gold) 50%, var(--gold-light));
  }
  .strap__rule--top    { top: 4px; }
  .strap__rule--bottom { bottom: 4px; }
  .strap--large .strap__rule { height: 4px; }
  .strap--large .strap__rule--top { top: 5px; }
  .strap--large .strap__rule--bottom { bottom: 5px; }

  .strap__pattern {
    position: absolute;
    left: 0; right: 0;
    top: 10px; bottom: 10px;
    background: linear-gradient(90deg,
      var(--strap-red-soft) 0%,
      var(--strap-red-deep) 15%,
      var(--strap-red-soft) 30%,
      var(--strap-red) 42%,
      var(--strap-red) 58%,
      var(--strap-red-soft) 70%,
      var(--strap-red-deep) 85%,
      var(--strap-red-soft) 100%);
  }
  .strap--large .strap__pattern { top: 12px; bottom: 12px; }

  .brand {
    position: absolute;
    left: 50%;
    top: 50%;
    transform: translate(-50%, -50%);
    display: flex;
    align-items: center;
    gap: 8px;
  }
  .brand__mark {
    flex: none;
    border-radius: 50%;
    border: 3px solid var(--gold);
  }
  .brand__text { display: flex; flex-direction: column; align-items: flex-start; }
  .brand__name {
    color: var(--gold);
    font-weight: 400;
    letter-spacing: 0.12em;
    line-height: 1;
  }
  .brand__tagline {
    color: var(--gold);
    font-weight: 500;
    letter-spacing: 0.14em;
    line-height: 1;
    margin-top: 3px;
  }

  .strap--spec .brand__mark { width: 36px; height: 36px; }
  .strap--spec .brand__name { font-size: 27px; }
  .strap--spec .brand__tagline { font-size: 9.5px; }

  .strap--large .brand__mark { width: 48px; height: 48px; }
  .strap--large .brand__name { font-size: 37px; }
  .strap--large .brand__tagline { font-size: 12.5px; margin-top: 4px; }
</style>
</head>
<body>
<main class="canvas">
  <span class="dimension dimension--left">20cm</span>
  <span class="dimension dimension--mid">42cm</span>
  <span class="dimension dimension--right">20cm</span>
  <span class="dimension dimension--height">6cm</span>

  <section class="strap strap--spec" aria-label="Label strap, flat layout with dimensions">
    <div class="strap__pattern" role="img" aria-label="Tone-on-tone red scroll ornament with vertical stripes"></div>
    <div class="strap__rule strap__rule--top"></div>
    <div class="strap__rule strap__rule--bottom"></div>
    <div class="brand">
      <span class="brand__mark"></span>
      <div class="brand__text">
        <span class="brand__name">KELVARO</span>
        <span class="brand__tagline">ONLINE PREMIUM FRUITS</span>
      </div>
    </div>
  </section>

  <section class="strap strap--large" aria-label="Label strap, full-width view">
    <div class="strap__pattern" role="img" aria-label="Tone-on-tone red scroll ornament with vertical stripes"></div>
    <div class="strap__rule strap__rule--top"></div>
    <div class="strap__rule strap__rule--bottom"></div>
    <div class="brand">
      <span class="brand__mark"></span>
      <div class="brand__text">
        <span class="brand__name">KELVARO</span>
        <span class="brand__tagline">ONLINE PREMIUM FRUITS</span>
      </div>
    </div>
  </section>
</main>
</body>
</html>
```